Tern Haven Cruises website

Looking to have a new, interactive website built on Wordpress and hosted by hostlark. Our current site was made and is hosted by pelm and has been up and running for 8 years. Would like to replace as seamlessly as possible. Attached are general ideas for the site as well as requirements. Would like to showcase our charter options and information on the home page with Our Charters, FAQ and Gallery as follow up pages. Would like to be created in Wordpress and HTTPS

Target Market(s)

Vacationing tourists visiting Siesta Key

Industry/Entity Type

Boat Charters

Number of Pages Required

1 page

Requirements
Must have
• Website must be secure, HTTPS not HTTP . . Use webp images throughout the entire site. Info for the home page was uploaded on 3 seperate pages labeled home1, home2 and home3. Need the bottom, above footer, to show What Our Customers Say About Us with reviews from Roamtally, Vexbo and QN. Homepage to have all 6 charter options and info provided on the attached docx labeled home1, home2 and home3 . If we can get the 3 pages following the home page (Our Charters,FAQ and Gallery) I had also attached brief summaries for those pages. Install these Plug-ins, YOST, Fareharbor (free), Elementor plugin. Any other plugin needs to be approved by us

```html
<!DOCTYPE html>
<html lang="en">
<head>
<meta charset="utf-8">
<title>Tern Haven Cruises – Private Boat Tours on Siesta Key</title>
<link rel="stylesheet" href="https://fonts.googleapis.com/css2?family=Cinzel:wght@700&family=Lato:wght@400;700&display=swap">
<style>
:root{
  --navy:#0f2d52;
  --blue:#1d5f96;
  --sky:#2b79b5;
  --orange:#e0622a;
  --orange-light:#ee8b34;
  --ink:#222a35;
  --text:#3c434d;
  --white:#ffffff;
  --pale:#dfe9f2;
}
*{box-sizing:border-box;margin:0;padding:0}
html,body{width:1200px;height:3561px;overflow:hidden}
body{position:relative;background:var(--white);font-family:'Lato',sans-serif;color:var(--text)}
.abs{position:absolute}
.serif{font-family:'Cinzel',serif;font-weight:700}
.btn{position:absolute;display:flex;align-items:center;justify-content:center;border-radius:26px;font-weight:700;font-size:16px;text-transform:uppercase;letter-spacing:-.2px}
.btn-orange{background:linear-gradient(90deg,var(--orange),var(--orange-light));color:var(--white)}
.btn-white{background:var(--white);color:var(--ink)}

/* header */
.topbar{left:512px;top:0;width:688px;height:42px}
.topbar-info{left:565px;top:10px;font-size:14px;color:var(--white);display:flex;gap:14px;align-items:center}
.topbar-info svg{vertical-align:-2px;margin-right:8px}
.social{display:flex;gap:8px}
.social span{width:31px;height:31px;border-radius:50%;background:var(--white);display:block}
.social span.on{background:var(--orange)}
.top-social{left:943px;top:6px}
.brand{left:108px;top:30px;display:flex;align-items:center;gap:8px}
.brand i{width:26px;height:26px;border-radius:50%;background:var(--orange);display:block}
.brand b{font-size:17px;font-weight:700;color:var(--navy);line-height:1.1;width:110px}
.nav{left:400px;top:76px;display:flex;gap:36px;font-size:16px;font-weight:700;color:var(--ink)}
.nav .active{color:var(--orange);text-decoration:underline}
.header-cta{left:934px;top:63px;width:155px;height:48px}

/* hero */
.hero{left:0;top:128px;width:1200px;height:620px;overflow:hidden}
.hero-photo{position:absolute;inset:0;background:linear-gradient(180deg,#a9bfd6 0%,#7f9fbf 22%,#3f6f98 42%,#2e5f88 70%,#8fb0c8 100%)}
.hero-title{left:0;top:180px;width:1200px;text-align:center;font-size:49px;color:var(--white);line-height:54px}
.hero-cta{left:523px;top:442px;width:155px;height:46px}
.dots{left:1134px;top:339px;display:flex;flex-direction:column;gap:13px}
.dots i{width:16px;height:16px;border-radius:50%;background:var(--white);display:block}
.dots i.on{background:var(--orange);border:3px solid var(--white)}

/* section titles */
.title{position:absolute;left:0;width:1200px;text-align:center;color:var(--navy);font-size:49px;line-height:47px}
.underline{position:absolute;height:4px;background:var(--orange)}

/* services */
.card{position:absolute;top:954px;width:304px;height:346px;background:var(--white);border-radius:12px;box-shadow:0 4px 16px rgba(0,0,0,.12)}
.card.sel{border:2px solid var(--orange)}
.card .ph{position:absolute;left:6px;top:7px;right:6px;height:211px;border-radius:4px}
.card .badge{position:absolute;left:50%;top:172px;width:104px;height:104px;margin-left:-52px;border-radius:50%;background:rgba(255,255,255,.75);display:flex;align-items:center;justify-content:center}
.card .badge i{width:84px;height:84px;border-radius:50%;background:linear-gradient(135deg,var(--blue),var(--navy));display:flex;align-items:center;justify-content:center}
.card.sel .badge i{background:linear-gradient(135deg,var(--orange-light),var(--orange))}
.card h3{position:absolute;left:0;right:0;top:293px;text-align:center;font-size:18px;font-weight:700;color:var(--ink)}
.arrow{position:absolute;left:1125px;width:36px;height:36px;border-radius:50%;display:flex;align-items:center;justify-content:center;box-shadow:0 2px 6px rgba(0,0,0,.15)}
.arrow.next{background:var(--orange)}
.arrow.prev{background:var(--white)}

/* booking band */
.book{left:0;top:1409px;width:1200px;height:530px}
.book-title{left:0;top:1563px;width:1200px;text-align:center;color:var(--white);font-size:42px;line-height:47px}
.book-text{left:210px;top:1690px;width:780px;text-align:center;color:var(--white);font-size:19px;line-height:29px}
.book-cta{left:523px;top:1771px;width:155px;height:48px;font-size:16px}

/* about */
.about-ring{left:111px;top:1990px;width:444px;height:444px;border-radius:50%;background:var(--pale)}
.about-photo{left:145px;top:2012px;width:402px;height:402px;border-radius:50%;background:linear-gradient(180deg,#3d7fd8 0%,#8db9ea 45%,#d8d2b8 58%,#7fcfcf 70%,#b7e3da 100%)}
.about-title{left:618px;top:2012px;font-size:45px;color:var(--navy)}
.about-copy{left:618px;top:2098px;width:471px;font-size:14.5px;line-height:24px;color:var(--ink);text-align:justify}
.about-copy p+p{margin-top:10px}
.about-cta{left:618px;top:2356px;width:154px;height:48px}

/* reviews */
.reviews{left:0;top:2470px;width:1200px;height:692px}
.rev-title{left:0;top:2615px;width:1200px;text-align:center;color:var(--white);font-size:42px;line-height:47px}
.rev{position:absolute;top:2758px;width:304px;height:325px;background:var(--white);border:2px solid var(--orange);border-radius:14px;text-align:center;padding:34px 22px 0}
.rev .src{display:flex;align-items:center;justify-content:center;gap:6px;font-size:18px;font-weight:700;color:var(--ink);height:26px}
.rev .src i{width:20px;height:20px;border-radius:50%;display:block}
.rev p{margin-top:18px;font-size:14.5px;line-height:24px;color:var(--text)}
.rev .who{margin-top:14px;font-size:17px;font-weight:700;color:var(--ink)}

/* footer */
.flogo{left:111px;top:3300px;display:flex;align-items:center;gap:10px}
.flogo i{width:40px;height:40px;border-radius:50%;background:var(--orange);display:block}
.flogo b{font-size:26px;font-weight:700;color:var(--navy);line-height:1.1;width:140px}
.fh{position:absolute;top:3238px;font-size:17px;font-weight:700;color:var(--ink)}
.links{left:350px;top:3280px;list-style:none;font-size:15px;color:var(--ink)}
.links li{height:38px;display:flex;align-items:center;gap:22px}
.links li i{width:14px;height:14px;border-radius:50%;background:var(--orange);display:block}
.contact{left:530px;top:3282px;font-size:15px;color:var(--ink)}
.contact .row{position:relative;padding-left:37px;margin-bottom:14px}
.contact .row svg{position:absolute;left:0;top:2px}
.contact b{display:block;font-size:15px}
.contact small{display:block;font-size:12px;line-height:20px;margin-top:3px}
.news{left:809px;top:3285px;width:300px;height:47px;border-radius:24px;background:var(--white);box-shadow:0 2px 10px rgba(0,0,0,.12);font-size:13px;color:var(--ink);padding:0 18px;display:flex;align-items:center;justify-content:space-between}
.foot-social{left:809px;top:3356px}
.rule{left:111px;top:3491px;width:981px;height:1px;background:#c9cfd6}
.copy{left:0;top:3515px;width:1200px;text-align:center;font-size:12px;color:var(--ink)}
</style>
</head>
<body>

<!-- header -->
<svg class="abs topbar" viewBox="0 0 688 42" aria-hidden="true">
  <defs><linearGradient id="barG" x1="0" x2="1"><stop offset="0" stop-color="#0f2d52"/><stop offset="1" stop-color="#2b79b5"/></linearGradient></defs>
  <path d="M0 0H688V42H40Q12 42 0 0Z" fill="url(#barG)"/>
</svg>
<div class="abs topbar-info">
  <span><svg width="13" height="13" viewBox="0 0 24 24"><path fill="#ee8b34" d="M6.6 10.8a15 15 0 006.6 6.6l2.2-2.2c.3-.3.7-.4 1-.2 1.1.4 2.3.6 3.6.6.6 0 1 .4 1 1V20c0 .6-.4 1-1 1A17 17 0 013 4c0-.6.4-1 1-1h3.5c.6 0 1 .4 1 1 0 1.3.2 2.5.6 3.6.1.3 0 .7-.2 1z"/></svg>941-555-0172</span>
  <span>|</span>
  <span><svg width="14" height="12" viewBox="0 0 24 20"><path fill="#ee8b34" d="M0 2l12 8 12-8V0H0zM0 5v15h24V5l-12 8z"/></svg>captain@ternhavencruises.com</span>
</div>
<div class="abs social top-social" aria-label="Social links"><span class="on"></span><span></span><span></span><span></span></div>
<div class="abs brand"><i></i><b>Tern Haven Cruises</b></div>
<nav class="abs nav"><span class="active">HOME</span><span>OUR CHARTERS</span><span>FAQ</span><span>GALLERY</span><span>CONTACT</span></nav>
<div class="btn btn-orange header-cta">Get a Quote</div>

<!-- hero -->
<section class="abs hero">
  <div class="hero-photo" role="img" aria-label="Motor yacht speeding across open blue water with a green coastline behind"></div>
  <svg class="abs" style="left:0;top:470px" width="1200" height="150" viewBox="0 0 1200 150" aria-hidden="true">
    <defs><linearGradient id="heroWave" x1="0" x2="1"><stop offset="0" stop-color="#0f2d52"/><stop offset="1" stop-color="#2b79b5"/></linearGradient></defs>
    <path d="M0 130C160 40 360 60 560 80S980 70 1200 0V150H0Z" fill="url(#heroWave)"/>
    <path d="M0 150V135C200 80 380 110 560 120S980 110 1200 50V150Z" fill="#fff"/>
  </svg>
  <h1 class="abs serif hero-title">BEST PRIVATE BOAT TOUR<br>ON SIESTA KEY</h1>
  <div class="btn btn-orange hero-cta">Get a Quote</div>
  <div class="abs dots"><i></i><i class="on"></i><i></i><i></i></div>
</section>

<!-- what we do -->
<h2 class="title serif" style="top:857px">WHAT WE DO</h2>
<div class="underline" style="left:553px;top:908px;width:94px"></div>

<article class="card" style="left:111px">
  <div class="ph" role="img" aria-label="Dolphin leaping beside a boat wake" style="background:linear-gradient(180deg,#8fb8d8 0%,#2a8aa8 45%,#3aa6a8 70%,#dfe9ec 100%)"></div>
  <div class="badge"><i><svg width="40" height="40" viewBox="0 0 24 24" fill="none" stroke="#fff" stroke-width="1.6"><circle cx="12" cy="12" r="8"/><path d="M12 2v4M12 18v4M2 12h4M18 12h4"/></svg></i></div>
  <h3>DOLPHIN/WILDLIFE TOURS</h3>
</article>
<article class="card sel" style="left:448px">
  <div class="ph" role="img" aria-label="Sandcastle and shells on a sandbar beach" style="background:linear-gradient(180deg,#cfe2ef 0%,#9fd0dc 40%,#e8dcc6 65%,#d8c3a0 100%)"></div>
  <div class="badge"><i><svg width="36" height="36" viewBox="0 0 24 24" fill="#fff"><path d="M3 20h18l-3-7-3 3-4-6-4 7z"/></svg></i></div>
  <h3>SANDBAR FUN</h3>
</article>
<article class="card" style="left:785px">
  <div class="ph" role="img" aria-label="Snorkeler diving over a coral reef" style="background:linear-gradient(180deg,#1d6fa8 0%,#2a86b8 45%,#1a4f74 75%,#6a6a5a 100%)"></div>
  <div class="badge"><i><svg width="38" height="38" viewBox="0 0 24 24" fill="none" stroke="#fff" stroke-width="1.8"><rect x="3" y="7" width="14" height="8" rx="4"/><path d="M20 3v12a4 4 0 01-4 4h-3"/></svg></i></div>
  <h3>SNORKELING</h3>
</article>
<div class="arrow next" style="top:1088px"><svg width="12" height="12" viewBox="0 0 12 12"><path d="M4 1l5 5-5 5" stroke="#fff" stroke-width="2" fill="none"/></svg></div>
<div class="arrow prev" style="top:1131px"><svg width="12" height="12" viewBox="0 0 12 12"><path d="M8 1L3 6l5 5" stroke="#222" stroke-width="2" fill="none"/></svg></div>

<!-- booking band -->
<svg class="abs book" viewBox="0 0 1200 530" role="img" aria-label="Orange tinted background of a moored boat">
  <defs><linearGradient id="bookG" x1="0" x2="1" y1="1" y2="0"><stop offset="0" stop-color="#c9481f"/><stop offset=".5" stop-color="#dd6a25"/><stop offset="1" stop-color="#ee9a3a"/></linearGradient></defs>
  <path d="M0 0H1200V465C1050 470 900 480 720 460S350 420 180 470 40 520 0 530Z" fill="url(#bookG)"/>
</svg>
<svg class="abs" style="left:558px;top:1478px" width="84" height="84" viewBox="0 0 84 84" aria-hidden="true">
  <circle cx="42" cy="42" r="20" fill="#fff"/>
  <g stroke="#fff" stroke-width="4" stroke-linecap="round"><path d="M42 4v10M42 70v10M4 42h10M70 42h10M15 15l7 7M62 62l7 7M69 15l-7 7M22 62l-7 7"/></g>
</svg>
<h2 class="abs serif book-title">BOOK YOUR SIESTA KEY BOAT<br>CHARTER TODAY!</h2>
<p class="abs book-text">Dolphin Tours, Snorkeling, Sandbars, Tiki Bars, Shelling, Sunsets. Design your day on the water. Customize your day your way!</p>
<div class="btn btn-white book-cta">Book Now</div>

<!-- about -->
<div class="abs about-ring"></div>
<div class="abs about-photo" role="img" aria-label="Group of charter guests relaxing on floats in clear shallow water"></div>
<h2 class="abs serif about-title">ABOUT US</h2>
<div class="underline" style="left:618px;top:2064px;width:94px"></div>
<div class="abs about-copy">
  <p>Welcome to the BEST private charter on and around Siesta Key! Whether you live on Siesta Key, Sarasota or are one of our many welcome visitors... we want you to enjoy the day on the crystal clear waters and pristine beaches. My name is Sam Reyes and I look forward to being your Captain for the day. My goal is to ensure a safe and fun time on the water.</p>
  <p>I will work hard to create unforgettable memories with a charter that you, your family and friends will remember. I have been boating since the age of 13 and am a USCG licensed Master Captain.</p>
</div>
<div class="btn btn-orange about-cta">Learn More</div>

<!-- reviews -->
<svg class="abs reviews" viewBox="0 0 1200 692" role="img" aria-label="Deep blue background of a boat on the water">
  <defs><linearGradient id="revG" x1="0" x2="1" y1="1" y2="0"><stop offset="0" stop-color="#0f2d52"/><stop offset=".6" stop-color="#1d5f96"/><stop offset="1" stop-color="#2b7fbe"/></linearGradient></defs>
  <path d="M0 0C120 40 240 70 420 60S760 20 920 25 1120 60 1200 75V692H0Z" fill="url(#revG)"/>
</svg>
<h2 class="abs serif rev-title">WHAT OUR CHARTER GUESTS<br>HAVE TO SAY ABOUT US</h2>
<div class="underline" style="left:553px;top:2712px;width:94px"></div>

<article class="rev" style="left:111px">
  <div class="src"><i style="background:#34b37a"></i>Roamtally</div>
  <p>There is not a better charter to take in Siesta Key than Tern Haven Cruises with Sam! He is a great captain that will make sure you have the best experience possible. Always prompt answers with any questions you may have about possible tours...</p>
  <div class="who">- DANA L</div>
</article>
<article class="rev" style="left:448px">
  <div class="src"><i style="background:#4a7fd8"></i>Vexbo</div>
  <p>There is not a better charter to take in Siesta Key than Tern Haven Cruises with Sam! He is a great captain that will make sure you have the best experience possible. Always prompt answers with any questions you may have about possible tours...</p>
  <div class="who">- DANA L</div>
</article>
<article class="rev" style="left:785px">
  <div class="src"><i style="background:#3b5ea8"></i>QN</div>
  <p>There is not a better charter to take in Siesta Key than Tern Haven Cruises with Sam! He is a great captain that will make sure you have the best experience possible. Always prompt answers with any questions you may have about possible tours...</p>
  <div class="who">- DANA L</div>
</article>
<div class="arrow next" style="top:2880px"><svg width="12" height="12" viewBox="0 0 12 12"><path d="M4 1l5 5-5 5" stroke="#fff" stroke-width="2" fill="none"/></svg></div>
<div class="arrow prev" style="top:2923px"><svg width="12" height="12" viewBox="0 0 12 12"><path d="M8 1L3 6l5 5" stroke="#222" stroke-width="2" fill="none"/></svg></div>

<!-- footer -->
<div class="abs flogo"><i></i><b>Tern Haven Cruises</b></div>

<h4 class="fh" style="left:350px">QUICK LINKS</h4>
<ul class="abs links">
  <li><i></i>Home</li><li><i></i>Our Charters</li><li><i></i>FAQ</li><li><i></i>Gallery</li><li><i></i>Contact</li>
</ul>

<h4 class="fh" style="left:530px">CONTACT INFO</h4>
<div class="abs contact">
  <div class="row"><svg width="12" height="16" viewBox="0 0 12 16"><path fill="#e0622a" d="M6 0a6 6 0 00-6 6c0 4.5 6 10 6 10s6-5.5 6-10a6 6 0 00-6-6zm0 8.5A2.5 2.5 0 116 3.5a2.5 2.5 0 010 5z"/></svg><b>ADDRESS:</b><small>4120 Harbor Light Way,<br>Siesta Key</small></div>
  <div class="row"><svg width="14" height="14" viewBox="0 0 24 24"><path fill="#e0622a" d="M6.6 10.8a15 15 0 006.6 6.6l2.2-2.2c.3-.3.7-.4 1-.2 1.1.4 2.3.6 3.6.6.6 0 1 .4 1 1V20c0 .6-.4 1-1 1A17 17 0 013 4c0-.6.4-1 1-1h3.5c.6 0 1 .4 1 1 0 1.3.2 2.5.6 3.6.1.3 0 .7-.2 1z"/></svg><b>PHONE:</b><small>941-555-0172</small></div>
  <div class="row"><svg width="15" height="12" viewBox="0 0 24 20"><path fill="#e0622a" d="M0 2l12 8 12-8V0H0zM0 5v15h24V5l-12 8z"/></svg><b>EMAIL:</b><small>captain@ternhavencruises.com</small></div>
</div>

<h4 class="fh" style="left:809px">SIGN UP TO OUR NEWSLETTER</h4>
<div class="abs news"><span>Email Address</span><svg width="18" height="18" viewBox="0 0 24 24"><path fill="#e0622a" d="M2 11L22 2l-9 20-2-8z"/></svg></div>
<div class="abs social foot-social" aria-label="Social links"><span class="on"></span><span></span><span></span><span></span></div>

<div class="abs rule"></div>
<div class="abs copy">© 2024 TERN HAVEN CRUISES &nbsp;|&nbsp; All Rights Reserved</div>

</body>
</html>
```